Presentation of Business Project of Implementing CRM for a car Detailing Company

We need a professional PowerPoint presentation template (5 slides) for a business presentation about implementing a CRM system at Ravenmoor Detailing, a premium automotive detailing company in South Africa.
About the Company:
Ravenmoor Detailing specializes in high-end car detailing, paint protection, leather repair, and classic car restoration. They're a premium service provider looking to modernize their customer management through digital transformation.
What We Need:
A visually impressive presentation template with 5 key slide designs that we can duplicate and reuse across our full presentation. The presentation will show how a ChatterLoop-integrated CRM system can help the business grow from 60% to 80% customer retention, free up the owner's time, and enable expansion.
The 5 Slides:

Title slide - Space for project title + 5 team member names (impactful opening)
Content slide - Standard layout with bullet points (we'll duplicate this for 10+ slides)
Large data table - For vendor comparisons (4 rows × 10 columns)
Financial charts - 3 side-by-side scenario comparisons with bar/column charts
Simple table - For cost breakdowns (2-3 columns)

Design Style:
Modern, polished, and eye-catching. Should look professional but capture attention - think sleek automotive industry meets premium business consulting. Bold use of car detailing/workshop imagery as backgrounds where appropriate. Contemporary color scheme. Clean layouts that make data easy to read but NOT boring.

Images:
We will provide a link to high-quality car detailing and workshop images that you can integrate into the design (backgrounds, accents, visual interest).

https://www.filebarrow-share.example/drive/7kqLm2TzvPeXn9RwY4HsJ-bGD#RavenmoorDetailing

Link contain image of company actual work and logo of the company. The idea is to use their images.

Important:
All tables and charts should be editable so we can add our own data. Slides should be easy to duplicate and modify.

Deliverables:
5 PowerPoint slides (.pptx) - fully editable
Google Slides version
Fonts/colors consistent throughout

```html
<!DOCTYPE html>
<html lang="en">
<head>
<meta charset="UTF-8">
<title>Ravenmoor Detailing – Presentation Template</title>
<link href="https://fonts.googleapis.com/css2?family=Poppins:wght@400;500;600;700;800&display=swap" rel="stylesheet">
<style>
  :root{
    --red:#d71920;
    --red-dark:#b3121a;
    --ink:#1c1c1f;
    --grey-dark:#4a4b52;
    --grey:#8a8b92;
    --grey-light:#c9cacd;
    --cell:#d5d6d9;
    --pink:#f0a9a9;
    --page:#a7a9ab;
    --white:#ffffff;
  }
  *{box-sizing:border-box;margin:0;padding:0}
  html,body{width:978px;height:1200px;overflow:hidden}
  body{background:var(--page);font-family:"Poppins",sans-serif;color:var(--ink)}
  .deck{position:relative;width:978px;height:1200px;display:grid;
    grid-template-columns:450px 450px;grid-template-rows:245px 245px 245px;
    column-gap:30px;row-gap:70px;padding:162px 24px 0}
  .slide{position:relative;background:var(--white);overflow:hidden;
    box-shadow:0 22px 18px -14px rgba(0,0,0,.35)}
  .brand-mark{display:flex;align-items:center;gap:5px;font-weight:600;color:var(--grey-dark)}
  .brand-mark .dot{border-radius:50%;border:2.5px solid var(--red);background:var(--white)}
  .slide-footer{position:absolute;left:22px;right:22px;bottom:18px;display:flex;align-items:center;gap:10px}
  .slide-footer .brand-mark{font-size:6px}
  .slide-footer .dot{width:14px;height:14px}
  .slide-footer .rule{flex:1;height:1px;background:var(--red)}
  .title-red{color:var(--red);font-weight:800;line-height:1.05}

  /* Title slide */
  .cover .photo{position:absolute;left:190px;top:0;width:260px;height:245px}
  .cover .brand-mark{position:absolute;left:22px;top:16px;flex-direction:column;gap:4px;font-size:8px;letter-spacing:1.6px}
  .cover .brand-mark .dot{width:30px;height:30px;border-width:4px}
  .cover .kicker{position:absolute;left:22px;top:86px;font-size:17px;font-weight:500;letter-spacing:.3px}
  .cover .big{position:absolute;left:20px;top:104px;font-size:42px}
  .cover .lede{position:absolute;left:22px;top:156px;width:170px;font-size:7.2px;line-height:1.55}
  .cover .meta{position:absolute;left:22px;bottom:19px;display:flex;gap:26px;font-size:6.6px}
  .cover .meta .label{color:var(--red);font-weight:600}
  .cover .web{color:var(--red);font-weight:500;letter-spacing:.6px}

  /* Team */
  .team .title-red{position:absolute;left:22px;top:18px;font-size:19px}
  .team .intro{position:absolute;left:147px;top:23px;width:238px;font-size:5.6px;line-height:1.55;text-align:justify}
  .team .members{position:absolute;left:28px;top:76px;display:flex;gap:11px}
  .member{width:62px;height:102px;border-radius:31px;background:var(--grey);position:relative;text-align:center;color:var(--white);padding-top:14px}
  .member:nth-child(even){background:var(--grey-dark)}
  .member .name{font-size:7px;font-weight:600;line-height:1}
  .member .role{font-size:5px;margin-top:2px}
  .member .portrait{position:absolute;left:0;bottom:0;width:62px;height:62px;border-radius:50%;
    background:radial-gradient(circle at 50% 40%,#e7e3df 0%,#9a9aa0 55%,#3d3e44 100%);border:3px solid var(--grey-dark)}

  /* Content */
  .content .photo{position:absolute;left:0;top:0;width:170px;height:100px}
  .content .title-red{position:absolute;left:20px;top:115px;font-size:19px}
  .content .body{position:absolute;left:20px;top:142px;width:132px;font-size:5.8px;line-height:1.55;text-align:justify}
  .content .spine{position:absolute;left:175px;top:22px;width:1px;height:130px;background:var(--red)}
  .points{position:absolute;left:172px;top:12px;display:flex;flex-direction:column;gap:7px}
  .point{display:flex;gap:6px;align-items:flex-start}
  .point .ico{flex:none;width:21px;height:21px;border-radius:50%;border:1.5px solid var(--grey-light);background:var(--white);
    display:flex;align-items:center;justify-content:center;margin-left:8px}
  .point .ico span{width:11px;height:11px;border-radius:50%;border:1.2px solid var(--red)}
  .point h3{font-size:6.2px;font-weight:600;margin-top:2px}
  .point p{font-size:5.6px;line-height:1.5;width:150px;margin-top:1px}

  /* Vendor table */
  .vendor .title-red{position:absolute;left:0;right:0;top:20px;text-align:center;font-size:19px}
  .vendor table{position:absolute;left:20px;top:56px;border-collapse:separate;border-spacing:1.5px;font-size:5px;text-align:center}
  .vendor th{background:var(--grey-light);font-weight:600;font-size:5.6px;height:10px;width:31.5px}
  .vendor th.corner{background:none;width:26px}
  .vendor td{background:var(--cell);height:25px;line-height:1.2}
  .vendor td.row-head{background:linear-gradient(90deg,var(--red-dark),#ef3b41);color:var(--white);font-weight:700;font-size:5.6px;border-radius:3px 0 0 3px}

  /* Chart */
  .chart .title-red{position:absolute;left:20px;top:18px;font-size:19px}
  .chart .sub{position:absolute;left:21px;top:42px;font-size:5.8px}
  .chart svg.plot{position:absolute;left:14px;top:56px;width:340px;height:90px}
  .legend{position:absolute;left:70px;top:153px;display:flex;gap:24px}
  .legend .item{display:flex;align-items:center;gap:4px;font-size:5.2px;line-height:1.1}
  .legend .sw{width:18px;height:18px;border-radius:50%}

  /* Cost */
  .cost .title-red{position:absolute;left:0;right:0;top:18px;text-align:center;font-size:19px}
  .cost .sub{position:absolute;left:0;right:0;top:42px;text-align:center;font-size:5.8px}
  .plans{position:absolute;left:75px;top:59px;display:flex;gap:9px}
  .plan{width:72px;height:100px;border-radius:4px;background:var(--white);border:1.5px solid var(--grey-dark);
    display:flex;flex-direction:column;align-items:center;overflow:hidden}
  .plan .head{width:100%;background:var(--grey-dark);color:var(--white);text-align:center;padding:4px 0 3px;line-height:1.15}
  .plan .head .t{font-size:6.4px}
  .plan .head .price{font-size:9.5px;font-weight:700}
  .plan .head .per{font-size:4.6px}
  .plan ul{list-style:none;font-size:6px;line-height:1.55;margin-top:4px;text-align:center}
  .plan .cta{margin-top:auto;width:100%;background:var(--grey-dark);padding:4px 0 5px;display:flex;justify-content:center}
  .plan .cta span{background:var(--white);color:var(--grey-dark);font-size:6px;font-weight:700;padding:0 4px;border-radius:1px}
  .plan.featured{border-color:var(--red);background:var(--red-dark)}
  .plan.featured .head,.plan.featured .cta{background:var(--red)}
  .plan.featured ul{color:var(--white)}
  .plan.featured .cta span{color:var(--red)}
  .plan.muted{border-color:var(--grey)}
  .plan.muted .head,.plan.muted .cta{background:var(--grey)}
  .plan.muted .cta span{color:var(--grey)}
</style>
</head>
<body>
<main class="deck">

  <!-- Title slide -->
  <section class="slide cover">
    <svg class="photo" viewBox="0 0 260 245" role="img" aria-label="Photo of a black sports car in the detailing workshop">
      <defs>
        <linearGradient id="shop" x1="0" y1="0" x2="0" y2="1">
          <stop offset="0" stop-color="#3a3b40"/>
          <stop offset=".55" stop-color="#1c1c20"/>
          <stop offset="1" stop-color="#6b6c70"/>
        </linearGradient>
      </defs>
      <path d="M7,0 L260,0 L260,245 C172,237 82,202 32,142 C2,102 -3,50 7,0 Z" fill="#d71920"/>
      <path d="M12,0 L260,0 L260,245 C176,236 88,200 38,140 C9,100 3,50 12,0 Z" fill="#9a9ba0"/>
      <path d="M16,0 L260,0 L260,245 C180,234 94,198 44,138 C15,98 7,50 16,0 Z" fill="url(#shop)"/>
    </svg>
    <div class="brand-mark"><span class="dot"></span>RAVENMOOR DETAILING</div>
    <div class="kicker">PRESENTATION</div>
    <div class="big title-red">NAME</div>
    <p class="lede">Lorem Ipsum is simply dummy text of the printing and typesetting industry.</p>
    <div class="meta">
      <span><span class="label">PRESENTED BY :</span> Name Here</span>
      <span class="web">&#9673; www.ravenmoordetailing.example</span>
    </div>
  </section>

  <!-- Team slide -->
  <section class="slide team">
    <h2 class="title-red">Our Team<br>Member</h2>
    <p class="intro">Lorem Ipsum is simply dummy text of the printing and typesetting industry. Lorem Ipsum has been the industry's standard dummy text ever since the 1500s, when an unknown printer took a galley of type and scrambled it to make a type specimen book.</p>
    <div class="members">
      <div class="member"><div class="name">Name Here</div><div class="role">Designation</div><div class="portrait" role="img" aria-label="Team member portrait"></div></div>
      <div class="member"><div class="name">Name Here</div><div class="role">Designation</div><div class="portrait" role="img" aria-label="Team member portrait"></div></div>
      <div class="member"><div class="name">Name Here</div><div class="role">Designation</div><div class="portrait" role="img" aria-label="Team member portrait"></div></div>
      <div class="member"><div class="name">Name Here</div><div class="role">Designation</div><div class="portrait" role="img" aria-label="Team member portrait"></div></div>
      <div class="member"><div class="name">Name Here</div><div class="role">Designation</div><div class="portrait" role="img" aria-label="Team member portrait"></div></div>
    </div>
    <footer class="slide-footer"><div class="brand-mark"><span class="dot"></span>Ravenmoor</div><span class="rule"></span></footer>
  </section>

  <!-- Content slide -->
  <section class="slide content">
    <svg class="photo" viewBox="0 0 170 100" role="img" aria-label="Photo of a sports car rear in the showroom">
      <defs>
        <linearGradient id="showroom" x1="0" y1="0" x2="0" y2="1">
          <stop offset="0" stop-color="#5b5c60"/>
          <stop offset=".6" stop-color="#26272b"/>
          <stop offset="1" stop-color="#9c9da0"/>
        </linearGradient>
      </defs>
      <path d="M0,0 L170,0 C170,50 160,90 130,100 L0,100 Z" fill="#d71920"/>
      <path d="M0,0 L165,0 C165,50 155,88 126,100 L0,100 Z" fill="url(#showroom)"/>
    </svg>
    <h2 class="title-red">Heading Here</h2>
    <p class="body">Lorem Ipsum is simply dummy text of the printing and typesetting industry. Lorem Ipsum has been the industry's .</p>
    <span class="spine"></span>
    <div class="points">
      <div class="point"><div class="ico"><span></span></div><div><h3>LOREM IPSUM 1</h3><p>Lorem Ipsum is simply dummy text of the printing and typesetting industry. Lorem Ipsum has been the industry's .</p></div></div>
      <div class="point"><div class="ico"><span></span></div><div><h3>LOREM IPSUM 1</h3><p>Lorem Ipsum is simply dummy text of the printing and typesetting industry. Lorem Ipsum has been the industry's .</p></div></div>
      <div class="point"><div class="ico"><span></span></div><div><h3>LOREM IPSUM 1</h3><p>Lorem Ipsum is simply dummy text of the printing and typesetting industry. Lorem Ipsum has been the industry's .</p></div></div>
      <div class="point"><div class="ico"><span></span></div><div><h3>LOREM IPSUM 1</h3><p>Lorem Ipsum is simply dummy text of the printing and typesetting industry. Lorem Ipsum has been the industry's .</p></div></div>
    </div>
    <footer class="slide-footer" style="right:20px;bottom:16px"><div class="brand-mark"><span class="dot"></span>Ravenmoor</div><span class="rule"></span></footer>
  </section>

  <!-- Vendor comparison table -->
  <section class="slide vendor">
    <h2 class="title-red">Vendor Comparisons</h2>
    <table>
      <thead><tr><th class="corner"></th><th>Ipsum</th><th>Ipsum</th><th>Ipsum</th><th>Ipsum</th><th>Ipsum</th><th>Ipsum</th><th>Ipsum</th><th>Ipsum</th><th>Ipsum</th><th>Ipsum</th></tr></thead>
      <tbody>
        <tr><td class="row-head">Lorem<br>1</td><td>Your text<br>here</td><td>Your text<br>here</td><td>Your text<br>here</td><td>Your text<br>here</td><td>Your text<br>here</td><td>Your text<br>here</td><td>Your text<br>here</td><td>Your text<br>here</td><td>Your text<br>here</td><td>Your text<br>here</td></tr>
        <tr><td class="row-head">Lorem<br>2</td><td>Your text<br>here</td><td>Your text<br>here</td><td>Your text<br>here</td><td>Your text<br>here</td><td>Your text<br>here</td><td>Your text<br>here</td><td>Your text<br>here</td><td>Your text<br>here</td><td>Your text<br>here</td><td>Your text<br>here</td></tr>
        <tr><td class="row-head">Lorem<br>3</td><td>Your text<br>here</td><td>Your text<br>here</td><td>Your text<br>here</td><td>Your text<br>here</td><td>Your text<br>here</td><td>Your text<br>here</td><td>Your text<br>here</td><td>Your text<br>here</td><td>Your text<br>here</td><td>Your text<br>here</td></tr>
        <tr><td class="row-head">Lorem<br>4</td><td>Your text<br>here</td><td>Your text<br>here</td><td>Your text<br>here</td><td>Your text<br>here</td><td>Your text<br>here</td><td>Your text<br>here</td><td>Your text<br>here</td><td>Your text<br>here</td><td>Your text<br>here</td><td>Your text<br>here</td></tr>
      </tbody>
    </table>
    <footer class="slide-footer" style="bottom:16px"><div class="brand-mark"><span class="dot"></span>Ravenmoor</div><span class="rule"></span></footer>
  </section>

  <!-- Scenario charts -->
  <section class="slide chart">
    <h2 class="title-red">Scenario Comparisons Charts</h2>
    <p class="sub">Lorem Ipsum is simply dummy text of the printing and typesetting industry</p>
    <svg class="plot" viewBox="0 0 340 90" font-family="Poppins, sans-serif" font-size="3.6" fill="#1c1c1f">
      <g stroke="#d5d6d9" stroke-width=".5">
        <line x1="20" y1="10" x2="330" y2="10"/><line x1="20" y1="21.7" x2="330" y2="21.7"/>
        <line x1="20" y1="33.3" x2="330" y2="33.3"/><line x1="20" y1="45" x2="330" y2="45"/>
        <line x1="20" y1="56.7" x2="330" y2="56.7"/><line x1="20" y1="68.3" x2="330" y2="68.3"/>
      </g>
      <line x1="20" y1="80" x2="330" y2="80" stroke="#4a4b52" stroke-width=".6"/>
      <line x1="20" y1="8" x2="20" y2="80" stroke="#4a4b52" stroke-width=".6"/>
      <g text-anchor="end">
        <text x="17" y="11">120</text><text x="17" y="22.7">100</text><text x="17" y="34.3">80</text>
        <text x="17" y="46">60</text><text x="17" y="57.7">40</text><text x="17" y="69.3">20</text><text x="17" y="81">0</text>
      </g>
      <g>
        <rect x="40" y="32.2" width="11" height="47.8" fill="#4a4b52"/>
        <rect x="52" y="21.7" width="11" height="58.3" fill="#8a8b92"/>
        <rect x="64" y="68.3" width="11" height="11.7" fill="#b0b1b5"/>
        <rect x="76" y="43.8" width="11" height="36.2" fill="#f0a9a9"/>
        <rect x="150" y="57.8" width="11" height="22.2" fill="#4a4b52"/>
        <rect x="162" y="32.2" width="11" height="47.8" fill="#8a8b92"/>
        <rect x="174" y="43.8" width="11" height="36.2" fill="#b0b1b5"/>
        <rect x="186" y="21.7" width="11" height="58.3" fill="#f0a9a9"/>
        <rect x="255" y="46.2" width="11" height="33.8" fill="#4a4b52"/>
        <rect x="267" y="36.3" width="11" height="43.7" fill="#8a8b92"/>
        <rect x="279" y="21.7" width="11" height="58.3" fill="#b0b1b5"/>
        <rect x="291" y="45" width="11" height="35" fill="#f0a9a9"/>
      </g>
      <g text-anchor="middle" font-size="3.2">
        <text x="45.5" y="30.7">82</text><text x="57.5" y="20.2">100</text><text x="69.5" y="66.8">20</text><text x="81.5" y="42.3">62</text>
        <text x="155.5" y="56.3">38</text><text x="167.5" y="30.7">82</text><text x="179.5" y="42.3">62</text><text x="191.5" y="20.2">100</text>
        <text x="260.5" y="44.7">58</text><text x="272.5" y="34.8">75</text><text x="284.5" y="20.2">100</text><text x="296.5" y="43.5">60</text>
      </g>
      <g text-anchor="middle" font-size="4.4">
        <text x="63.5" y="87">2023</text><text x="173.5" y="87">2024</text><text x="278.5" y="87">2025</text>
      </g>
    </svg>
    <div class="legend">
      <div class="item"><span class="sw" style="background:var(--grey-dark)"></span>Lorem<br>Ipsum</div>
      <div class="item"><span class="sw" style="background:var(--grey)"></span>Lorem<br>Ipsum</div>
      <div class="item"><span class="sw" style="background:#b0b1b5"></span>Lorem<br>Ipsum</div>
      <div class="item"><span class="sw" style="background:var(--pink)"></span>Lorem<br>Ipsum</div>
    </div>
    <footer class="slide-footer" style="bottom:16px"><div class="brand-mark"><span class="dot"></span>Ravenmoor</div><span class="rule"></span></footer>
  </section>

  <!-- Cost breakdowns -->
  <section class="slide cost">
    <h2 class="title-red">Cost Breakdowns</h2>
    <p class="sub">Lorem Ipsum is simply dummy text of the printing and typesetting industry</p>
    <div class="plans">
      <div class="plan">
        <div class="head"><div class="t">Lorem Ipsum</div><div class="price">430 zar</div><div class="per">Per Month</div></div>
        <ul><li>Lorem ipsum</li><li>Lorem ipsum</li><li>Lorem ipsum</li><li>Lorem ipsum</li></ul>
        <div class="cta"><span>Get Started</span></div>
      </div>
      <div class="plan featured">
        <div class="head"><div class="t">Lorem Ipsum</div><div class="price">540 zar</div><div class="per">Per Month</div></div>
        <ul><li>Lorem ipsum</li><li>Lorem ipsum</li><li>Lorem ipsum</li><li>Lorem ipsum</li></ul>
        <div class="cta"><span>Get Started</span></div>
      </div>
      <div class="plan muted">
        <div class="head"><div class="t">Lorem Ipsum</div><div class="price">320 zar</div><div class="per">Per Month</div></div>
        <ul><li>Lorem ipsum</li><li>Lorem ipsum</li><li>Lorem ipsum</li><li>Lorem ipsum</li></ul>
        <div class="cta"><span>Get Started</span></div>
      </div>
    </div>
    <footer class="slide-footer" style="bottom:16px"><div class="brand-mark"><span class="dot"></span>Ravenmoor</div><span class="rule"></span></footer>
  </section>

</main>
</body>
</html>
```